Store Front Sign for Vape Store

Interested in getting a store front sign graphic done. Sign is for over the door (lighted sign). Dimensions of sign: 6 feet long x 2 feet high.
Sign is for a Vape Store. I have attached the logo to be used.
Looking for a modern and professional look
Phone numbers to be used.
Whatsapp# 364-9105
Contact #519-7036
Sign should have Instagram & Facebook logos and. handle @lagoonmistco

Industry/Entity Type

Vape | Electronic Cigarettes

Colors

Designer to choose colors to be used in the design.

Requirements
Must have
• Facebook and Instagram Logos. Contact Numbers.
Should not have
• Any Persons.

```html
<!DOCTYPE html>
<html lang="en">
<head>
<meta charset="utf-8">
<title>Lagoon Mist Co – Storefront Sign</title>
<link href="https://fonts.googleapis.com/css2?family=Montserrat:wght@500;600&display=swap" rel="stylesheet">
<style>
  :root {
    --page: #eceff1;
    --sign-dark: #2a2829;
    --sign-pattern: #312f30;
    --ink-black: #161616;
    --lagoon-blue: #00a8e1;
    --lagoon-deep: #0a7fb5;
    --silver-light: #ffffff;
    --silver-mid: #c9cdd0;
    --text-light: #ffffff;
  }
  * { margin: 0; padding: 0; box-sizing: border-box; }
  html, body {
    width: 1200px; height: 889px; overflow: hidden;
    background: var(--page);
    font-family: "Montserrat", sans-serif;
  }
  .sign {
    position: absolute; left: 30px; top: 254px;
    width: 1140px; height: 380px;
    background: var(--sign-dark);
    overflow: hidden;
    box-shadow: 0 10px 30px rgba(0,0,0,.25);
  }
  .sign__texture {
    position: absolute; inset: 0;
    background: radial-gradient(ellipse at 50% 40%, var(--sign-pattern), var(--sign-dark) 75%);
  }
  .sign__waves { position: absolute; inset: 0; }
  .contact {
    position: absolute; left: 130px; top: 100px;
    display: flex; flex-direction: column; gap: 20px;
  }
  .contact__row { display: flex; align-items: center; gap: 18px; }
  .contact__icon { width: 44px; height: 44px; flex: none; }
  .contact__number {
    color: var(--text-light); font-weight: 500; font-size: 36px; letter-spacing: 1px;
  }
  .brand {
    position: absolute; left: 488px; top: 40px;
    width: 290px; height: 290px; border-radius: 50%;
    background: radial-gradient(circle at 50% 40%, #3a3a3b, #1c1c1d 75%);
    border: 6px solid var(--lagoon-blue);
    display: flex; align-items: center; justify-content: center; text-align: center;
  }
  .brand__name {
    color: var(--silver-mid); font-weight: 600; font-size: 40px; line-height: 1.15;
  }
  .social {
    position: absolute; right: 40px; top: 192px; width: 200px;
    display: flex; flex-direction: column; align-items: center; gap: 12px;
  }
  .social__icons { display: flex; gap: 12px; }
  .social__dot {
    width: 30px; height: 30px; border-radius: 50%;
    background: var(--lagoon-blue);
  }
  .social__handle { color: var(--text-light); font-weight: 500; font-size: 22px; }
</style>
</head>
<body>
  <div class="sign">
    <div class="sign__texture" role="img" aria-label="Subtle dark hexagon texture across the sign face"></div>

    <svg class="sign__waves" viewBox="0 0 1140 380" preserveAspectRatio="none" aria-hidden="true">
      <defs>
        <linearGradient id="silverBand" x1="0" x2="1" y1="0" y2="0">
          <stop offset="0" stop-color="var(--silver-mid)"/>
          <stop offset=".4" stop-color="var(--silver-light)"/>
          <stop offset="1" stop-color="var(--silver-mid)"/>
        </linearGradient>
        <linearGradient id="blueBand" x1="0" x2="1" y1="0" y2="0">
          <stop offset="0" stop-color="var(--lagoon-blue)"/>
          <stop offset=".7" stop-color="var(--lagoon-blue)"/>
          <stop offset="1" stop-color="var(--lagoon-deep)"/>
        </linearGradient>
      </defs>
      <path d="M0 225 C300 190 550 260 780 330 C950 380 1080 360 1140 288 L1140 380 L0 380 Z" fill="url(#silverBand)"/>
      <path d="M0 250 C300 214 550 288 780 352 C950 398 1080 378 1140 312 L1140 380 L0 380 Z" fill="var(--ink-black)"/>
      <path d="M0 268 C320 234 560 320 790 374 C950 408 1080 386 1140 334 L1140 380 L0 380 Z" fill="url(#blueBand)"/>
    </svg>

    <div class="contact">
      <div class="contact__row">
        <svg class="contact__icon" viewBox="0 0 44 44" aria-label="Phone">
          <circle cx="22" cy="22" r="22" fill="var(--lagoon-blue)"/>
          <path d="M15 11 l5 0 l2 7 l-3 2 c1.5 3.5 3.5 5.5 7 7 l2 -3 l7 2 l0 5 c-12 1 -21 -8 -20 -20 z" fill="var(--ink-black)"/>
        </svg>
        <span class="contact__number">519-7036</span>
      </div>
      <div class="contact__row">
        <svg class="contact__icon" viewBox="0 0 44 44" aria-label="Messaging">
          <circle cx="22" cy="22" r="22" fill="var(--lagoon-blue)"/>
        </svg>
        <span class="contact__number">364-9105</span>
      </div>
    </div>

    <div class="brand">
      <span class="brand__name">Lagoon<br>Mist Co</span>
    </div>

    <div class="social">
      <div class="social__icons">
        <span class="social__dot"></span>
        <span class="social__dot"></span>
      </div>
      <span class="social__handle">@lagoonmistco</span>
    </div>
  </div>
</body>
</html>
```